BENEATH THE [HARBOR] OF A DAWN, Mend your road

We are looking for a cover refresh of an existing bestselling book that is going into 3rd edition print this year.
The book is an inspirational as well as educational book that has become recognized as one of the most comprehensive, actionable, personal and financial planning resources available today for families, individuals and business owners alike.
Comprised of three true stories of loss, learning to live and love again and a 30 page checklist at the back of the book it contains tips and strategies for everyone to help them to get their personal and financial lives in order while they can.
The cover must have the following:
1. Appeal to a broad audience/both personal and corporate
2. Include Mara Quellton Bestselling Author
3. Include introduction of a new Afterword
4. 3rd Edition
5. Colors to remain the same – red, black and white
6. The title must remain in caps and the word [HARBOR] must have the brackets around it
We have also added a current copy of the second edition to help you. For your information our website is www.thequelltonhouse.example
Reason: We have narrowed it down to our top 3 designs. We are submitting the covers to our community for them to pick the top cover. Good luck to everyone

```html
<!DOCTYPE html>
<html lang="en">
<head>
<meta charset="utf-8">
<title>Beneath the Harbor of a Dawn — Mara Quellton</title>
<link rel="stylesheet" href="https://fonts.googleapis.com/css2?family=Cinzel:wght@400&family=Allura&display=swap">
<style>
  :root {
    --cover-red: #b6212a;
    --cover-red-deep: #8c1d22;
    --cover-black: #1d1a1b;
    --band-black: #141213;
    --band-glow: #3a3637;
    --paper: #ffffff;
    --ink: #1c1a1a;
    --muted: #5a5657;
    --art-dark: #2a2627;
    --art-gold: #c9a24e;
    --art-silver: #d4d2cf;
  }
  html, body {
    margin: 0;
    padding: 0;
    width: 800px;
    height: 1200px;
    overflow: hidden;
    background: var(--cover-black);
  }
  .cover {
    position: relative;
    width: 800px;
    height: 1200px;
    overflow: hidden;
    background: linear-gradient(180deg, var(--cover-red) 0%, var(--cover-red) 30%, var(--cover-red-deep) 55%, var(--cover-black) 85%);
    font-family: "Cinzel", serif;
  }
  .page {
    position: absolute;
    left: 26px;
    top: 23px;
    width: 747px;
    height: 986px;
    background: var(--paper);
    clip-path: polygon(325px 0, 100% 0, 100% 100%, 0 100%, 0 226px);
  }
  .edition-flag {
    position: absolute;
    left: 58px;
    top: 150px;
    transform: rotate(-36deg);
    transform-origin: left top;
    color: var(--paper);
    text-align: center;
    line-height: 1.05;
    font-size: 30px;
    font-weight: 400;
  }
  .edition-flag sup { font-size: 17px; text-transform: lowercase; }
  .pen-art {
    position: absolute;
    left: 489px;
    top: 23px;
    width: 284px;
    height: 256px;
    background: linear-gradient(215deg, var(--art-dark) 0%, var(--art-dark) 30%, var(--art-gold) 55%, var(--art-silver) 80%, var(--paper) 100%);
    opacity: 0.9;
  }
  .title {
    margin: 0;
    font-weight: 400;
    color: var(--ink);
  }
  .title-line, .title-key {
    position: absolute;
    left: 0;
    width: 800px;
    text-align: center;
    line-height: 1;
    font-weight: 400;
    white-space: nowrap;
  }
  .title-line { font-size: 74px; }
  .title-first { top: 380px; }
  .title-last { top: 583px; }
  .title-key {
    top: 450px;
    font-size: 132px;
    color: var(--cover-red);
  }
  .title-key .bracket { font-size: 150px; vertical-align: -6px; }
  .title-key .dark { color: var(--ink); }
  .subtitle {
    position: absolute;
    left: 0;
    top: 690px;
    width: 800px;
    margin: 0;
    text-align: center;
    font-family: "Allura", cursive;
    font-size: 100px;
    line-height: 1.1;
    color: var(--ink);
  }
  .afterword-note {
    position: absolute;
    left: 0;
    top: 900px;
    width: 800px;
    margin: 0;
    text-align: center;
    font-size: 22px;
    letter-spacing: 3px;
    color: var(--cover-red);
  }
  .author-band {
    position: absolute;
    left: 0;
    top: 1009px;
    width: 800px;
    height: 191px;
    background: radial-gradient(ellipse at 50% 40%, var(--band-glow) 0%, var(--band-black) 70%);
    text-align: center;
  }
  .author-name {
    margin: 36px 0 0;
    font-size: 58px;
    font-weight: 400;
    color: var(--paper);
    letter-spacing: 1px;
  }
  .author-tag {
    margin: 6px 0 0;
    font-size: 30px;
    color: var(--muted);
    letter-spacing: 1px;
  }
</style>
</head>
<body>
  <main class="cover">
    <div class="page"></div>
    <div class="edition-flag">3<sup>rd</sup><br>EDITION</div>
    <div class="pen-art" role="img" aria-label="Fountain pen with a black barrel and a gold and silver nib pointing down toward the title"></div>

    <h1 class="title">
      <span class="title-line title-first">BENEATH THE</span>
      <span class="title-key"><span class="bracket">[</span>HARB<span class="dark">O</span>R<span class="bracket">]</span></span>
      <span class="title-line title-last">OF A DAWN</span>
    </h1>
    <p class="subtitle">Mend your road</p>
    <p class="afterword-note">WITH A NEW AFTERWORD</p>

    <footer class="author-band">
      <p class="author-name">MARA QUELLTON</p>
      <p class="author-tag">BESTSELLING AUTHOR</p>
    </footer>
  </main>
</body>
</html>
```